Restaurant needs a vertical banner for fried catfish

Our restaurant is looking for an eye-catching 78.75in. x 36in. vertical physical banner ad for our fried catfish. Photos for the fried catfish will be provided as a reference but we will also accept anything similar to the photo. We will be using the following as our receptacle: https://www.plankoria.example/banner-stand/retractable-banner-stands/
The design must incorporate the following flavor texts:
Fried Catfish
Always Fresh!
Made from Scratch
Hand-cut Fillets
The Best Catfish in Texas
Served with fries, hush puppies, and a 32oz fountain drink
Also available by the pound!
The final design should be creative, professional, and eye-catching for customers.
Updates
Colors
Designer to choose colors to be used in the design.
Requirements
Must have
- We are open to any and all design elements, albeit the 'flavor texts' should not overpower, but complement the fried catfish photo. 'Fried Catfish' can be used in lieu of a main title/logo.
Nice to have
- Transparent or textured backgrounds that can encompass any or all part of the banner such as a cutting board, shadows, abstract, etc to show depth are a plus.
- Use of vectors or objects such as ribbons or shapes to encapsulate the 'flavor texts' are also encouraged.

```html
<!DOCTYPE html>
<html lang="en">
<head>
<meta charset="utf-8">
<title>Fried Catfish Vertical Banner</title>
<link rel="stylesheet" href="https://fonts.googleapis.com/css2?family=Bitter:wght@400;500;700&family=Lobster&display=swap">
<style>
  :root {
    --stage: #858585;
    --board-light: #ffffff;
    --board-shade: #ececec;
    --ink: #39434d;
    --green: #4ba94b;
    --yellow: #f8cb10;
    --yellow-dark: #e0b300;
    --white: #ffffff;
    --photo-dark: #2f3a42;
    --photo-mid: #4a5258;
    --photo-warm: #8a5a2b;
  }
  html, body {
    margin: 0;
    padding: 0;
    width: 1200px;
    height: 1025px;
    overflow: hidden;
    background: var(--stage);
  }
  .banner {
    position: absolute;
    left: 375px;
    top: 20px;
    width: 450px;
    height: 985px;
    box-shadow: 0 4px 18px rgba(0,0,0,0.3);
  }
  .script { font-family: 'Lobster', cursive; }
  .slab { font-family: 'Bitter', serif; }
  .headline { font-weight: 500; fill: var(--ink); }
  .green-text { fill: var(--green); }
  .white-text { fill: var(--white); }
  .ink-text { fill: var(--ink); }
</style>
</head>
<body>
<svg class="banner" viewBox="0 0 450 985" width="450" height="985" xmlns="http://www.w3.org/2000/svg">
  <defs>
    <linearGradient id="boardGrad" x1="0" y1="0" x2="1" y2="0">
      <stop offset="0" stop-color="var(--board-shade)"/>
      <stop offset="0.5" stop-color="var(--board-light)"/>
      <stop offset="1" stop-color="var(--board-shade)"/>
    </linearGradient>
    <radialGradient id="photoGrad" cx="0.45" cy="0.55" r="0.7">
      <stop offset="0" stop-color="var(--photo-warm)"/>
      <stop offset="0.55" stop-color="var(--photo-mid)"/>
      <stop offset="1" stop-color="var(--photo-dark)"/>
    </radialGradient>
  </defs>

  <!-- background boards -->
  <rect class="board" x="0" y="0" width="450" height="985" fill="url(#boardGrad)"/>

  <!-- title -->
  <text class="script green-text" x="223" y="60" font-size="46" text-anchor="middle">fried</text>
  <text class="slab headline" x="224" y="140" font-size="84" text-anchor="middle" textLength="348" lengthAdjust="spacingAndGlyphs">CATFISH</text>

  <!-- food photo with green swoosh frame -->
  <path class="swoosh-top" d="M0,268 Q190,160 450,164 L450,190 Q220,184 0,292 Z" fill="var(--green)"/>
  <path class="food-photo" role="img" aria-label="Photo of fried catfish fillets with fries, hush puppies, dipping sauce and lemons on a wooden board"
        d="M0,296 Q220,192 450,196 L450,552 Q250,632 0,610 Z" fill="url(#photoGrad)"/>
  <path class="swoosh-bottom" d="M0,620 Q250,642 450,562 L450,588 Q250,666 0,644 Z" fill="var(--green)"/>

  <!-- badge -->
  <g class="badge">
    <circle cx="89" cy="252" r="72" fill="var(--yellow)" stroke="var(--white)" stroke-width="3"/>
    <text class="script white-text" x="89" y="228" font-size="25" text-anchor="middle">The Best</text>
    <text class="script white-text" x="89" y="260" font-size="25" text-anchor="middle">Catfish</text>
    <text class="script white-text" x="89" y="292" font-size="25" text-anchor="middle">in Texas</text>
  </g>

  <!-- main message -->
  <text class="slab headline" x="224" y="711" font-size="58" text-anchor="middle" textLength="364" lengthAdjust="spacingAndGlyphs">Fried Catfish</text>
  <text class="script green-text" x="226" y="767" font-size="42" text-anchor="middle">- Always Fresh! -</text>

  <!-- ribbon -->
  <g class="ribbon">
    <path d="M23,826 L70,819 L78,854 L36,856 L46,840 Z" fill="var(--yellow-dark)"/>
    <path d="M432,826 L385,819 L377,854 L419,856 L409,840 Z" fill="var(--yellow)"/>
    <path d="M55,800 L405,800 L395,846 L65,846 Z" fill="var(--yellow)"/>
    <text class="slab white-text" x="226" y="817" font-size="17" text-anchor="middle">Served with fries, hush puppies,</text>
    <text class="slab white-text" x="226" y="837" font-size="17" text-anchor="middle">and a 32oz fountain drink</text>
  </g>

  <!-- checklist -->
  <g class="checklist">
    <rect x="25" y="880" width="14" height="14" rx="2" fill="none" stroke="var(--green)" stroke-width="1.8"/>
    <path d="M28,886 L32,891 L41,878" fill="none" stroke="var(--green)" stroke-width="2.2" stroke-linecap="round"/>
    <text class="slab ink-text" x="50" y="894" font-size="18">Made from Scratch</text>
    <rect x="255" y="880" width="14" height="14" rx="2" fill="none" stroke="var(--green)" stroke-width="1.8"/>
    <path d="M258,886 L262,891 L271,878" fill="none" stroke="var(--green)" stroke-width="2.2" stroke-linecap="round"/>
    <text class="slab ink-text" x="280" y="894" font-size="18">Hand-cut Fillets</text>
  </g>

  <!-- footer bar -->
  <rect class="footer-bar" x="0" y="919" width="450" height="39" fill="var(--green)"/>
  <text class="slab white-text" x="225" y="946" font-size="22" text-anchor="middle">Also available by the pound!</text>
</svg>
</body>
</html>
```